We are a printed circuit board manufacturer. Need a company professional web site to allow our potential customers to know more about our background, capability and our products. The web site will contain three languages, which are Chinese, English and Japanese. Our audience are mainly electronic companies that procure printed circuit boards. I have a word document that have all the required text in all three languages. The final design should communicate the impression that we embrace quality, trustworthiness and long term partnership business principles.
We should have sections that allow us to post pictures of our facilities.
I have added the three files in three different languages.
Some of the information is below:
Background
RVD Worldwide Limited (RVD) was set up in Hong Kong in 2007 by two Hong Kong entrepreneurs, Mr. Lok Fai Tam and Mr. Wai Ho. We acquired the single sided printed circuit board factory located in Dongguan City, Guangdong Province, China, from Valtor Corporation of the U.S. in 2007. In addition to RVD, Mr. Tam and Mr. Ho also own Brightrail Systems Company Limited, a semiconductor company based in Hong Kong since 1997 with a total investment of over US$100 million. Brightrail is engaged in the manufacturing of flexible substrates and MEMS assembly business.
RVD has been awarded TS 16949 and ISO14000 certificates since 2009 and 2004 respectively.
Business Principles
RVD Worldwide Limited strives to be a professional top notched printed circuit board supplier. We embrace four “EXCELLENCE” principles, namely, excellence in quality, excellence in prices, excellence in services and excellence in on time delivery.
We approach each customer with a long-term partnership view that delivers the lowest ownership costs and highest total values to our customers. We customize quotations and solutions in order to allow our customers to win more businesses. We believe by thinking from our customers’ points of view we will be able to create a WIN-WIN relationship.
Customers
Due to our excellent quality, services and production systems, RVD Worldwide Limited manage to service a number of large Japanese and US customers, which include:
Technical capability overview
Below is an overview of our current capability:
Target Market(s)
Electronic companies buyers
Industry/Entity Type
Business
Requirements
Must have
- Capability description
Should not have
- no cartoon

```html
<!DOCTYPE html>
<html lang="en">
<head>
<meta charset="utf-8">
<title>RVD Worldwide Limited</title>
<link href="https://fonts.googleapis.com/css2?family=Arimo:wght@400;700&family=Yanone+Kaffeesatz:wght@400&family=Michroma&display=swap" rel="stylesheet">
<style>
:root{
  --green:#1f6b58;
  --green-dark:#17574a;
  --olive:#2f3a26;
  --olive-line:#56604c;
  --page:#ffffff;
  --band:#f3f3f3;
  --card:#f7f7f7;
  --card-line:#e2e2e2;
  --text:#333;
  --muted:#777;
  --nav:#555;
  --accent-red:#c8251f;
  --accent-blue:#1a3f9a;
  --accent-green:#2a8a4a;
}
*{box-sizing:border-box;margin:0;padding:0}
html,body{width:901px;height:1200px;overflow:hidden;background:var(--page)}
body{position:relative;font-family:"Arimo",Arial,sans-serif;color:var(--text)}
.abs{position:absolute}

.brand{left:83px;top:52px;width:176px;text-align:center;color:var(--green);font-weight:700}
.brand .name{font-size:34px;letter-spacing:4px;line-height:38px}
.brand .sub{font-size:13px;color:var(--olive);letter-spacing:1px;line-height:15px}

.nav{left:364px;top:46px;width:470px;display:grid;grid-template-columns:134px 99px 105px 61px 71px;row-gap:13px;font-family:"Yanone Kaffeesatz",sans-serif;font-size:15px;color:var(--nav)}
.nav a{display:flex;align-items:center;gap:5px;height:27px;border-bottom:1px solid #ddd;margin-right:9px;text-decoration:none;color:inherit;white-space:nowrap}
.nav a::before{content:"";width:9px;height:9px;background:#d8d8d8;flex:none}

.slider{left:85px;top:146px;width:743px;height:263px;background:var(--olive);border:1px solid #20281a}
.slider .photo{left:0;top:0;width:433px;height:218px;background:linear-gradient(135deg,#cfc9c4,#9ea4a6 55%,#6f7678)}
.slider .panel{left:433px;top:0;width:308px;height:218px;background:linear-gradient(160deg,#1f6b58,#17574a 60%,#2a7a66);color:#fff}
.panel h1{position:absolute;left:36px;top:40px;font-size:14px;font-weight:700;white-space:nowrap}
.panel p{position:absolute;left:88px;top:74px;width:180px;font-size:9.5px;line-height:16.6px;text-align:justify}
.dots{left:16px;top:228px;display:flex;gap:6px}
.dots span{width:17px;height:17px;background:#fff;font-size:8px;font-weight:700;display:flex;align-items:center;justify-content:center;color:#000}
.slider .more{right:22px;top:229px;width:81px;height:21px;background:#f1f1f1;color:var(--green-dark);font-size:12px;display:flex;align-items:center;justify-content:center;box-shadow:0 1px 2px #000}
.shadow{left:150px;top:407px;width:600px;height:22px;background:radial-gradient(ellipse at top,rgba(0,0,0,.22),transparent 70%)}

.band{left:0;top:462px;width:901px;height:515px;background:var(--band);border-top:2px solid #e6e6e6}
.tab{left:372px;top:459px;width:145px;height:29px;background:#fff;border:1px solid #ddd;border-top:none;font-family:"Michroma",sans-serif;font-size:14px;color:var(--olive);display:flex;align-items:center;justify-content:center;letter-spacing:2px;white-space:nowrap}

.card{width:333px;height:189px;background:var(--card);border:1px solid var(--card-line);border-radius:3px;box-shadow:0 2px 3px rgba(0,0,0,.06)}
.card h2{position:absolute;left:14px;top:10px;font-size:16.5px;font-weight:700;color:var(--text);white-space:nowrap}
.card ul{position:absolute;left:27px;top:40px;list-style:none;font-size:10.5px;color:var(--muted);line-height:21px}
.card .pic{position:absolute;right:12px;top:24px;width:129px;height:106px;border:1px solid #ccc;box-shadow:0 1px 3px rgba(0,0,0,.2)}
.card .pic.low{top:34px;right:14px}
.pic.orange{background:linear-gradient(90deg,#c2542a 0 45%,#b9bcbf 45%)}
.pic.gray{background:linear-gradient(135deg,#b7b2ae,#e2e2e0 50%,#8c9294)}
.card .read{position:absolute;right:30px;bottom:16px;font-size:10.5px;font-weight:700;color:var(--green-dark);display:flex;align-items:center;gap:7px}
.read i{width:17px;height:17px;border-radius:50%;background:#c4c4c4;display:flex;align-items:center;justify-content:center}

.cust-title{left:365px;top:975px;width:160px;height:26px;background:#fff;font-family:"Michroma",sans-serif;font-size:12px;color:var(--olive);letter-spacing:1px;white-space:nowrap;display:flex;align-items:center;justify-content:center}
.logos{left:76px;top:1027px;width:730px;height:34px;display:flex;align-items:center;justify-content:space-between}
.logos .name{font-family:"Arimo",sans-serif;font-size:18px;font-weight:700;display:flex;align-items:center;gap:6px;white-space:nowrap}
.arrow{width:16px;height:16px;border:1px solid #999;border-radius:50%;display:flex;align-items:center;justify-content:center}

.footer{left:0;top:1085px;width:901px;height:115px;background:var(--olive);color:#dcdcd0;font-size:9.5px}
.flinks{position:absolute;left:75px;top:23px;width:395px;display:grid;grid-template-columns:117px 79px 93px 55px 51px}
.flinks span{height:29px;line-height:27px;border-bottom:1px solid var(--olive-line);padding-left:2px;white-space:nowrap}
.copy{position:absolute;left:555px;top:24px;font-size:8.5px;white-space:nowrap}
.social{position:absolute;left:720px;top:52px;display:flex;gap:6px}
.social span{width:44px;height:44px;background:#111;border-radius:6px;border:1px solid #000}
</style>
</head>
<body>

<div class="abs brand"><div class="name">RVD</div><div class="sub">Worldwide Limited</div></div>

<nav class="abs nav">
  <a>About The Company</a><a>Customers</a><a>Raw Materials</a><a>Plating</a><a>Carbon</a>
  <a>Punching &amp; CNC Process</a><a>Printing Proces</a><a>Surface Finishing</a><a>V-Cut</a><a>Contact Us</a>
</nav>

<section class="abs slider">
  <div class="abs photo" role="img" aria-label="Factory production line with control cabinets"></div>
  <div class="abs panel">
    <h1>Welcome to RVD Worldwide Limited</h1>
    <p>RVD Worldwide Limited (RVD) was set up in Hong Kong in 2007 by two Hong Kong entrepreneurs, Mr. Lok Fai Tam and Mr. Wai Ho. We acquired the single sided printed circuit board factory located in Dongguan City, Guangdong Province, China, from Valtor Corporation of the U.S. in 2007.</p>
  </div>
  <div class="abs dots"><span>1</span><span>2</span><span>3</span></div>
  <div class="abs more">Read More</div>
</section>
<div class="abs shadow"></div>

<section class="abs band"></section>
<div class="abs tab">FEATURES</div>

<article class="abs card" style="left:83px;top:517px">
  <h2>Raw Materials</h2>
  <ul><li>Paper Phenolic</li><li>Paper Epoxy</li><li>Glass Epoxy</li><li>Overall Thickness (T) &nbsp; Customer</li><li>Copper Thickness</li></ul>
  <div class="pic orange" role="img" aria-label="Raw material processing machine"></div>
  <div class="read">Read More <i><svg width="7" height="8"><path d="M0 0L7 4L0 8Z" fill="#fff"/></svg></i></div>
</article>
<article class="abs card" style="left:464px;top:517px">
  <h2>Printing Processes</h2>
  <ul><li>Screen Printing</li><li>Minimum Track Width (W)</li><li>Minimum Line Spacing (W)</li><li>Minimum of Annular Ring</li><li>Etching</li><li>S/M clearance from Copper (W)</li></ul>
  <div class="pic gray" role="img" aria-label="Printing process equipment"></div>
  <div class="read">Read More <i><svg width="7" height="8"><path d="M0 0L7 4L0 8Z" fill="#fff"/></svg></i></div>
</article>
<article class="abs card" style="left:83px;top:737px">
  <h2>Surface Finishing</h2>
  <ul><li>Surface Finishing</li><li>Conductive</li><li>Protective Coating</li><li>Ionic Contamination &nbsp;Cleanout</li></ul>
  <div class="pic orange" role="img" aria-label="Surface finishing machine"></div>
  <div class="read">Read More <i><svg width="7" height="8"><path d="M0 0L7 4L0 8Z" fill="#fff"/></svg></i></div>
</article>
<article class="abs card" style="left:464px;top:737px">
  <h2>Punching And CNC Process</h2>
  <ul style="top:46px;line-height:19.5px"><li>Outline Dimension</li><li>Hole Position Accuracy</li><li>Hole Diameter Accuracy</li><li>Minimum Punching Hole Size</li><li>Minimum Rectangular Slot Size</li><li>Paper Epoxy &amp; Glass Epoxy</li></ul>
  <div class="pic gray low" role="img" aria-label="CNC punching equipment"></div>
  <div class="read">Read More <i><svg width="7" height="8"><path d="M0 0L7 4L0 8Z" fill="#fff"/></svg></i></div>
</article>

<div class="abs cust-title">OUR CUSTOMERS</div>
<div class="abs logos">
  <span class="arrow"><svg width="6" height="8"><path d="M6 0L0 4L6 8Z" fill="#777"/></svg></span>
  <span class="name" style="color:#222">Norberg Industrial</span>
  <span class="name" style="color:var(--accent-red)">Velmora</span>
  <span class="name" style="color:#111">KORVEX</span>
  <span class="name" style="color:var(--accent-blue)">Lumatron</span>
  <span class="name" style="color:var(--accent-green)">Akemi</span>
  <span class="name" style="color:#c47a2a;font-size:12px">Qarden</span>
  <span class="arrow"><svg width="6" height="8"><path d="M0 0L6 4L0 8Z" fill="#777"/></svg></span>
</div>

<footer class="abs footer">
  <div class="flinks">
    <span>About The Company</span><span>Customers</span><span>Raw Materials</span><span>Plating</span><span>Carbon</span>
    <span>Punching &amp; CNC Process</span><span>Printing Proces</span><span>Surface Finishing</span><span>V-Cut</span><span>Contact Us</span>
  </div>
  <div class="copy">© 2012 &nbsp;&nbsp; Copyright. &nbsp;RVD Worldwide Limited .All Rights Reserved</div>
  <div class="social"><span aria-label="Chirper"></span><span aria-label="Pagebook"></span></div>
</footer>

</body>
</html>
```